Design Business Card

I'm looking for a creative and modern looking business card that matches up to our "Vornadex Software" logo. Business card should utilize the same orange, blue and gray colors that the logo uses. In addition, this contest requires both front and back side of the card - it must look professional and creative. Please feel free to check out our website http://www.vornadex.com to find out more about us.

```html
<!DOCTYPE html>
<html lang="en">
<head>
<meta charset="utf-8">
<title>Vornadex Software – Business Card</title>
<link rel="stylesheet" href="https://fonts.googleapis.com/css2?family=Lato:wght@400;700;900&display=swap">
<style>
  :root{
    --stage:#4a5059;
    --card:#262729;
    --card-edge:#1b1c1d;
    --orange:#f5a623;
    --blue:#4a90d9;
    --white:#f2f2f2;
    --muted:#bfbfbf;
  }
  *{margin:0;padding:0;box-sizing:border-box}
  html,body{width:1200px;height:900px;overflow:hidden}
  body{background:var(--stage);font-family:"Lato",sans-serif;position:relative}
  .card{
    position:absolute;width:540px;height:310px;border-radius:26px;
    background:var(--card);box-shadow:0 6px 0 var(--card-edge),0 18px 30px rgba(0,0,0,.35);
  }
  .card--front{left:50px;top:480px}
  .card--back{left:610px;top:110px}

  /* front */
  .holder{position:absolute;left:40px;top:36px}
  .holder__name{display:flex;align-items:center;gap:8px;font-size:22px;color:var(--white)}
  .holder__name .last{color:var(--orange)}
  .holder__role{font-size:13px;color:var(--orange);margin-left:24px;margin-top:2px}
  .front-mark{position:absolute;left:40px;top:140px;display:flex;align-items:center;gap:8px}
  .mark-dot{width:16px;height:16px;border-radius:50%;background:var(--blue)}
  .mark-name{font-weight:900;font-size:17px;color:var(--orange)}
  .contacts{position:absolute;left:262px;top:112px;list-style:none}
  .contacts li{display:flex;align-items:center;gap:10px;color:var(--white);font-size:16px;height:34px}
  .contacts svg{width:18px;height:18px;flex:none}
  .social{position:absolute;right:40px;bottom:30px;display:flex;gap:12px}
  .social span{width:24px;height:24px;border-radius:5px;background:var(--orange)}

  /* back */
  .back-mark{position:absolute;inset:0;display:flex;align-items:center;justify-content:center;gap:14px}
  .back-mark .mark-dot{width:30px;height:30px}
  .back-mark .mark-name{font-size:36px}
</style>
</head>
<body>
  <section class="card card--front">
    <div class="holder">
      <p class="holder__name">
        <svg width="14" height="14" viewBox="0 0 14 14" aria-hidden="true"><rect x="0" y="0" width="6" height="6" fill="#f2f2f2"/><rect x="8" y="8" width="6" height="6" fill="#f2f2f2"/></svg>
        <span>Marcus <span class="last">Hale</span></span>
      </p>
      <p class="holder__role">President</p>
    </div>
    <div class="front-mark">
      <span class="mark-dot"></span>
      <span class="mark-name">Vornadex Software</span>
    </div>
    <ul class="contacts">
      <li>
        <svg viewBox="0 0 24 24" aria-hidden="true"><path d="M6 3l3 0 1.5 5-2 1.5a12 12 0 0 0 6 6l1.5-2 5 1.5v3a2 2 0 0 1-2 2A17 17 0 0 1 4 5a2 2 0 0 1 2-2z" fill="none" stroke="#f2f2f2" stroke-width="1.8"/></svg>
        +1-555-014-2278
      </li>
      <li>
        <svg viewBox="0 0 24 24" aria-hidden="true"><rect x="2" y="5" width="20" height="14" fill="none" stroke="#f2f2f2" stroke-width="1.8"/><path d="M2 5l10 8 10-8" fill="none" stroke="#f2f2f2" stroke-width="1.8"/></svg>
        info@vornadex.com
      </li>
      <li>
        <svg viewBox="0 0 24 24" aria-hidden="true"><circle cx="12" cy="12" r="9.5" fill="none" stroke="#f2f2f2" stroke-width="1.8"/><ellipse cx="12" cy="12" rx="4" ry="9.5" fill="none" stroke="#f2f2f2" stroke-width="1.5"/><path d="M2.5 12h19M4 7h16M4 17h16" stroke="#f2f2f2" stroke-width="1.3"/></svg>
        www.vornadex.com
      </li>
    </ul>
    <div class="social" aria-label="Social profiles">
      <span></span><span></span><span></span>
    </div>
  </section>

  <section class="card card--back">
    <div class="back-mark">
      <span class="mark-dot"></span>
      <span class="mark-name">Vornadex Software</span>
    </div>
  </section>
</body>
</html>
```